Business cards, e-mail signature, letterhead
Noral Studio, Inc
Business cards, e-mail signature, letterhead - Communications and Media
Creative Brief
Bright & Fun-filled
Tobin Varley
President, Noral Studio Inc.
Card: New York City Letterhead: 47 West 112th St. 9F New York, NY 10031
skype: tobinvarley604
tbnvrl@quillpost.net
www.NoralStudio.com
Locations of our properties can be listed on the back of card (see below) and incorporated into letterhead.
Ash Fork, AZ / Ashtabula, OH/ Belle Rose, LA/ Blanca, CO/ Cross City, FL/ Dulac, LA/ Huntington, OR/ Islamorada, FL/ Lead, SD/ Mona, UT/ Morgan, GA/ Ty Ty, GA/ Winchester, VA

```html
<!DOCTYPE html>
<html lang="en">
<head>
<meta charset="utf-8">
<title>Noral Studio, Inc — Business Card</title>
<link href="https://fonts.googleapis.com/css2?family=Open+Sans:wght@400;600;700&family=Oswald:wght@500&display=swap" rel="stylesheet">
<style>
  :root{
    --backdrop:#e6e7eb;
    --card:#ffffff;
    --navy:#27266f;
    --navy-deep:#1b1a55;
    --navy-soft:#4a4aa0;
    --ink:#3a3a4a;
    --muted:#7a7a88;
  }
  *{box-sizing:border-box;margin:0;padding:0}
  html,body{width:1200px;height:864px;overflow:hidden}
  body{background:var(--backdrop);font-family:"Open Sans",sans-serif;color:var(--ink);position:relative}
  .card{position:absolute;width:540px;height:309px;background:var(--card);border-radius:14px;overflow:hidden;box-shadow:0 6px 18px rgba(30,30,60,.18)}
  .card--front{left:40px;top:277px}
  .card--back{left:620px;top:277px}

  /* front */
  .front-mark{position:absolute;left:0;right:0;top:88px;display:flex;flex-direction:column;align-items:center;gap:10px}
  .mark-dot{width:70px;height:70px;border-radius:50%;background:var(--navy)}
  .brand-name{font-family:"Oswald",sans-serif;font-weight:500;color:var(--navy);letter-spacing:.06em;text-transform:uppercase}
  .front-mark .brand-name{font-size:15px}
  .front-url{position:absolute;left:0;right:0;top:232px;text-align:center;font-size:11px;letter-spacing:.32em;color:var(--muted)}

  /* back */
  .swoosh{position:absolute;inset:0;width:540px;height:309px}
  .back-brand{position:absolute;left:26px;top:170px;display:flex;align-items:center;gap:10px}
  .back-brand .mark-dot{width:34px;height:34px}
  .back-brand .brand-name{font-size:15px;line-height:1}
  .tagline{display:block;font-family:"Open Sans",sans-serif;font-size:8px;letter-spacing:.2em;color:var(--muted);text-transform:lowercase;margin-top:3px}
  .contact-list{position:absolute;left:30px;top:218px;list-style:none;font-size:9px;line-height:1.2;color:var(--ink)}
  .contact-list li{display:flex;align-items:center;gap:7px;margin-bottom:3px}
  .contact-icon{width:11px;height:11px;flex:none}
  .person{position:absolute;right:28px;top:40px;text-align:right}
  .person-name{font-size:13px;font-weight:700;color:var(--navy)}
  .person-title{font-size:9.5px;color:var(--muted);margin-top:2px}
</style>
</head>
<body>

<section class="card card--front" aria-label="Card front">
  <div class="front-mark">
    <span class="mark-dot" aria-hidden="true"></span>
    <span class="brand-name">Noral Studio, Inc</span>
  </div>
  <p class="front-url">www.NoralStudio.com</p>
</section>

<section class="card card--back" aria-label="Card back">
  <svg class="swoosh" viewBox="0 0 540 309" aria-hidden="true">
    <path d="M0,0 H380 C320,40 240,60 180,105 C130,140 70,158 0,162 Z" fill="var(--navy)"/>
    <path d="M380,0 C320,40 240,60 180,105 C130,140 70,158 0,162 L0,168 C74,164 136,146 186,110 C246,66 330,42 392,0 Z" fill="var(--navy-soft)" opacity=".55"/>
    <path d="M0,0 H300 C250,30 190,48 140,82 C100,108 50,118 0,120 Z" fill="var(--navy-deep)" opacity=".45"/>
  </svg>

  <div class="person">
    <p class="person-name">Tobin Varley</p>
    <p class="person-title">President, Noral Studio Inc.</p>
  </div>

  <div class="back-brand">
    <span class="mark-dot" aria-hidden="true"></span>
    <div>
      <span class="brand-name">Noral Studio Inc.</span>
      <span class="tagline">creative, improved</span>
    </div>
  </div>

  <ul class="contact-list">
    <li>
      <svg class="contact-icon" viewBox="0 0 12 12" aria-hidden="true"><circle cx="6" cy="6" r="6" fill="var(--navy)"/><path d="M6 2.6a2.2 2.2 0 0 0-2.2 2.2C3.8 6.6 6 9.4 6 9.4s2.2-2.8 2.2-4.6A2.2 2.2 0 0 0 6 2.6z" fill="#fff"/></svg>
      <span>47 West 112th St. 9F New York, NY 10031</span>
    </li>
    <li>
      <svg class="contact-icon" viewBox="0 0 12 12" aria-hidden="true"><circle cx="6" cy="6" r="6" fill="var(--navy)"/><path d="M4 3h1.3l.6 1.6-.8.6a4 4 0 0 0 1.7 1.7l.6-.8L9 6.7V8a1 1 0 0 1-1 1A5 5 0 0 1 3 4a1 1 0 0 1 1-1z" fill="#fff"/></svg>
      <span>(646) 555-0182</span>
    </li>
    <li>
      <svg class="contact-icon" viewBox="0 0 12 12" aria-hidden="true"><circle cx="6" cy="6" r="6" fill="var(--navy)"/></svg>
      <span>tobinvarley604</span>
    </li>
    <li>
      <svg class="contact-icon" viewBox="0 0 12 12" aria-hidden="true"><circle cx="6" cy="6" r="6" fill="var(--navy)"/><rect x="3" y="4" width="6" height="4.2" fill="none" stroke="#fff" stroke-width=".9"/><path d="M3 4l3 2.3L9 4" fill="none" stroke="#fff" stroke-width=".9"/></svg>
      <span>tbnvrl@quillpost.net</span>
    </li>
    <li>
      <svg class="contact-icon" viewBox="0 0 12 12" aria-hidden="true"><circle cx="6" cy="6" r="6" fill="var(--navy)"/><circle cx="6" cy="6" r="3" fill="none" stroke="#fff" stroke-width=".9"/><path d="M3 6h6M6 3c-1.2 1.6-1.2 4.4 0 6M6 3c1.2 1.6 1.2 4.4 0 6" fill="none" stroke="#fff" stroke-width=".7"/></svg>
      <span>www.NoralStudio.com</span>
    </li>
  </ul>
</section>

</body>
</html>
```